International Company needs a Letterhead & Envelope Design

Our Company name is Corvale Brightwick Limited.
We'd like to ask the Designers for the luxurious and sophisticated design. Our logo is very simple and neat with letter logos, so we look forward to more professional and refined designs from Designers.
We look forward to providing you with a great design.
Thanks very much in advance.

```html
<!DOCTYPE html>
<html lang="en">
<head>
<meta charset="utf-8">
<title>Corvale Brightwick Limited — Letterhead</title>
<link href="https://fonts.googleapis.com/css2?family=Arimo:wght@400;700&display=swap" rel="stylesheet">
<style>
  :root {
    --ink: #333335;
    --brand-grey: #4a4a4c;
    --paper: #ffffff;
  }
  * { margin: 0; padding: 0; box-sizing: border-box; }
  html, body { width: 927px; height: 1200px; overflow: hidden; background: var(--paper); }
  .letterhead {
    position: relative;
    width: 927px;
    height: 1200px;
    font-family: "Arimo", Arial, sans-serif;
    color: var(--ink);
  }
  .brand-name {
    position: absolute;
    font-weight: 700;
    color: var(--brand-grey);
    text-transform: uppercase;
    line-height: 1.05;
    letter-spacing: 0.5px;
  }
  .brand-name--top { left: 19px; top: 20px; font-size: 21px; }
  .brand-name--bottom { left: 669px; top: 1132px; font-size: 21px; text-align: right; width: 238px; }
  .rule {
    position: absolute;
    background: var(--brand-grey);
  }
  .rule--top { left: 270px; top: 17px; width: 657px; height: 7px; }
  .rule--bottom { left: 0; top: 1168px; width: 660px; height: 8px; }
  .rule--contact { left: 593px; top: 50px; width: 3px; height: 107px; }
  .contact-icons {
    position: absolute;
    left: 609px;
    top: 52px;
    display: flex;
    flex-direction: column;
    gap: 17px;
  }
  .contact-icons svg { width: 22px; height: 22px; display: block; }
  .body-copy {
    position: absolute;
    left: 130px;
    font-size: 15.6px;
    line-height: 20.5px;
    white-space: nowrap;
  }
  .body-copy .line { display: block; }
  .body-copy .line--indent { padding-left: 83px; }
  .body-copy .line--indent-wide { padding-left: 88px; }
  .sign-off {
    position: absolute;
    left: 700px;
    top: 966px;
    font-size: 15.6px;
    line-height: 20.5px;
  }
</style>
</head>
<body>
<div class="letterhead">
  <div class="brand-name brand-name--top">Corvale Brightwick<br>Limited</div>
  <div class="rule rule--top"></div>

  <div class="rule rule--contact"></div>
  <div class="contact-icons" aria-label="Contact details">
    <svg viewBox="0 0 24 24" fill="none" stroke="#4a4a4c" stroke-width="1.8" aria-label="Phone">
      <circle cx="12" cy="12" r="10.5"/>
      <path d="M8.2 6.8l1.8-.4 1.2 2.8-1.3 1a6.5 6.5 0 0 0 3.9 3.9l1-1.3 2.8 1.2-.4 1.8c-.2.7-.9 1.1-1.6 1A9.5 9.5 0 0 1 7.2 8.4c-.1-.7.3-1.4 1-1.6z" stroke-linejoin="round"/>
    </svg>
    <svg viewBox="0 0 24 24" fill="none" stroke="#4a4a4c" stroke-width="1.8" aria-label="Email">
      <circle cx="12" cy="12" r="10.5"/>
      <rect x="6.5" y="8" width="11" height="8" rx="0.5"/>
      <path d="M6.8 8.4L12 12.6l5.2-4.2M6.8 15.6l3.6-3.2M17.2 15.6l-3.6-3.2"/>
    </svg>
    <svg viewBox="0 0 24 24" fill="none" stroke="#4a4a4c" stroke-width="1.8" aria-label="Address">
      <circle cx="12" cy="12" r="10.5"/>
      <path d="M12 18.2s-4.2-4.3-4.2-7.3a4.2 4.2 0 0 1 8.4 0c0 3-4.2 7.3-4.2 7.3z" stroke-linejoin="round"/>
      <circle cx="12" cy="10.9" r="1.5"/>
    </svg>
  </div>

  <div class="body-copy" style="top:247px">
    <span class="line line--indent">Hi there shfhdsbgsdgsdgjbsdjbvjsg sdg usdhgusdhughsdu fuudgfgdsfgsu dffs dgusdug</span>
    <span class="line">dfh sdygfysdgdgufuadsuhfhud guhsdughsdiuighsudhgushdughsduhgsd</span>
    <span class="line">gsdhgh sdsguysaagd fsdsg faudgf asgfadfhdfhdfushfuashfygasuyufgadfakgfsdfuhsdf</span>
    <span class="line">sfsisadf gysydgfyusdgfudgfsdsgdfiddgfiuusdidufhdsfdjskbfsdgfidgsfuigdsuivsd</span>
    <span class="line">fsagfsyudgfsdyufbsdhfvuyuysdgfsdiyfgdsufgadsfsasdgfiasgdfiudsgdfisdfuu</span>
  </div>

  <div class="body-copy" style="top:369px">
    <span class="line line--indent">Hi there shfhdsbgsdgsdgjbsdjbvjsg sdg usdhgusdhughsdu fuudgfgdsfgsu dffs dgusdug</span>
    <span class="line">dfh sdygfysdgdgufuadsuhfhud guhsdughsdiuighsudhgushdughsduhgsd</span>
    <span class="line">gsdhgh sdsguysaagd fsdsg faudgf asgfadfhdfhdfushfuashfygasuyufgadfakgfsdfuhsdf</span>
    <span class="line">sfsisadf gysydgfyusdgfudgfsdsgdfiddgfiuusdidufhdsfdjskbfsdgfidgsfuigdsuivsd</span>
    <span class="line">fsagfsyudgfsdyufbsdhfvuyuysdgfsdiyfgdsufgadsfsasdgfiasgdfiudsgdfisdfuu</span>
  </div>

  <div class="body-copy" style="top:492px">
    <span class="line line--indent">Hi there shfhdsbgsdgsdgjbsdjbvjsg sdg usdhgusdhughsdu fuudgfgdsfgsu dffs dgusdug</span>
    <span class="line">dfh sdygfysdgdgufuadsuhfhud guhsdughsdiuighsudhgushdughsduhgsd</span>
    <span class="line">gsdhgh sdsguysaagd fsdsg faudgf asgfadfhdfhdfushfuashfygasuyufgadfak</span>
  </div>

  <div class="body-copy" style="top:593px">
    <span class="line line--indent">sfsisadf gysydgfyusdgfudgfsdsgdfiddgfiuusdidufhdsfdjskbfsdgfidgsfuigdsuivsd</span>
    <span class="line">fsagfsyudgfsdyufbsdhfvuyuysdgfsdiyfgdsufgadsfsasdgfiasgdfiudsgdfisdfuuHi there</span>
    <span class="line">shfhdsbgsdgsdgjbsdjbvjsg sdg usdhgusdhughsdu fuudgfgdsfgsu dffs dg</span>
  </div>

  <div class="body-copy" style="top:695px">
    <span class="line line--indent-wide">dfh sdygfysdgdgufuadsuhfhud guhsdughsdiuighsudhgushdughsduhgsd</span>
    <span class="line">gsdhgh sdsguysaagd fsdsg faudgf asgfadfhdfhdfushfuashfygasuyufgadfakgfsdfuhsdf</span>
    <span class="line">sfsisadf gysydgfyusdgfudgfsdsgdfiddgfiuusdidufhdsfdjskbfsdgf.</span>
  </div>

  <div class="body-copy" style="top:776px">
    <span class="line line--indent-wide">dfh sdygfysdgdgufuadsuhfhud guhsdughsdiuighsudhgushdughsduhgsd</span>
    <span class="line">gsdhgh sdsguysaagd fsdsg faudgf asgfadfhdfhdfushfuashfygasuyufgadfakgfsdfuhsdf</span>
    <span class="line">sfsisadf gysydgfyusdgfudgfsdsgdfiddgfiuusdidufhdsfdjskbfsdgf.</span>
  </div>

  <div class="body-copy" style="top:858px">
    <span class="line line--indent-wide">dfh sdygfysdgdgufuadsuhfhud guhsdughsdiuighsudhgushdughsduhgsd</span>
    <span class="line">gsdhgh sdsguysaagd fsdsg faudgf asgfadfhdfhdfushfuashfygasuyufgadfakgfsdfuhsdf</span>
    <span class="line">sfsisadf gysydgfyusdgfudgfsdsgdfiddgfiuusdidufhdsfdjskbfsdgf.</span>
  </div>

  <div class="sign-off">Your sincerely<br>Tarin Velloway</div>

  <div class="rule rule--bottom"></div>
  <div class="brand-name brand-name--bottom">Corvale Brightwick<br>Limited</div>
</div>
</body>
</html>
```